Supplement Bottle Packaging and Design

We want to rebrand our current health supplements (see below). We do want it to be modern, vibrant and appealing supplement bottles. Very upscale and elegant as it targets primarily women.
NOTE: READ THE ATTACHED WORD DOCUMENT!
Bottle size: We are totally open to the bottle size and shape, as long it's a typical supplement bottle size to handle 90-120 capsules; what we mostly need is new bottle design/packaging. YOU DON’T HAVE TO USE THE CURRENT WHITE BOTTLE SHAPE, BUT ANYTHING MORE MODERN WOULD WORK!
Updates
We need more modern, clean sleek designs to choose from
Look and feel
Each slider illustrates characteristics of the customer's brand and the style your logo design should communicate.

```html
<!DOCTYPE html>
<html lang="en">
<head>
<meta charset="utf-8">
<title>Supplement Label Series</title>
<link rel="stylesheet" href="https://fonts.googleapis.com/css2?family=Lato:wght@400;700;900&display=swap">
<style>
  :root {
    --canvas: #f3f1ee;
    --ink-grey: #4a4a4a;
    --liver: #8e3a6e;
    --liver-band: #d06aa0;
    --liver-badge-a: #6f2756;
    --liver-badge-b: #a1477f;
    --tummy: #c40f2b;
    --tummy-band: #c8102e;
    --tummy-badge-a: #a30c22;
    --tummy-badge-b: #de2a3f;
    --hormone: #127a2a;
    --hormone-band: #1b8a1f;
    --hormone-badge-a: #0f6e20;
    --hormone-badge-b: #2aa034;
    --sugar: #1b2a9e;
    --sugar-band: #0d1a7d;
    --sugar-badge-a: #0d1a7d;
    --sugar-badge-b: #2235b0;
    --white: #ffffff;
  }
  * { box-sizing: border-box; margin: 0; padding: 0; }
  html, body { width: 1200px; height: 1200px; overflow: hidden; }
  body {
    background: var(--canvas);
    font-family: "Lato", sans-serif;
    position: relative;
  }
  .label {
    position: absolute;
    left: 233px;
    width: 733px;
    height: 243px;
    overflow: hidden;
    box-shadow: 0 4px 14px rgba(0,0,0,0.12);
  }
  .label--liver { top: 25px; }
  .label--tummy { top: 316px; }
  .label--hormone { top: 600px; }
  .label--sugar { top: 894px; }

  .label__art { position: absolute; inset: 0; }
  .label--liver .label__art {
    background: radial-gradient(circle at 12% 30%, #c9a8e0 0%, transparent 35%),
                radial-gradient(circle at 88% 25%, #d6b8ea 0%, transparent 30%),
                linear-gradient(135deg, #e6d4f2 0%, #f6eef8 50%, #ecd9f1 100%);
  }
  .label--tummy .label__art {
    background: radial-gradient(circle at 5% 80%, #f4a6a6 0%, transparent 30%),
                radial-gradient(circle at 92% 25%, #f29a9a 0%, transparent 32%),
                linear-gradient(135deg, #f3e6e6 0%, #f7efef 50%, #f1e3e3 100%);
  }
  .label--hormone .label__art {
    background: radial-gradient(circle at 8% 30%, #9ec4b4 0%, transparent 30%),
                radial-gradient(circle at 92% 40%, #a9cdbf 0%, transparent 28%),
                linear-gradient(135deg, #eef5f1 0%, #fafcfb 50%, #edf4f0 100%);
  }
  .label--sugar .label__art {
    background: radial-gradient(circle at 10% 45%, #7cc3e6 0%, transparent 32%),
                radial-gradient(circle at 80% 50%, #86c9ea 0%, transparent 32%),
                linear-gradient(135deg, #d8eef9 0%, #f1f9fd 50%, #d9eef9 100%);
  }

  .label__wave { position: absolute; left: 0; bottom: 0; width: 733px; height: 243px; }

  .label__title {
    position: absolute;
    left: 230px;
    top: 36px;
    font-size: 40px;
    line-height: 1;
    font-weight: 700;
    letter-spacing: 0.5px;
    white-space: nowrap;
  }
  .label--tummy .label__title { top: 38px; }
  .label--hormone .label__title { font-size: 36px; top: 64px; }
  .label--sugar .label__title { font-size: 28px; top: 50px; }

  .label__subtitle {
    position: absolute;
    left: 230px;
    top: 90px;
    font-size: 15px;
    line-height: 19px;
    color: var(--ink-grey);
  }
  .label--liver .label__subtitle { top: 90px; }
  .label--hormone .label__subtitle { top: 108px; }

  .label__badge {
    position: absolute;
    top: 157px;
    width: 169px;
    height: 53px;
    border-radius: 9px;
    color: var(--white);
    text-align: center;
    box-shadow: 0 2px 4px rgba(0,0,0,0.25);
    padding-top: 5px;
  }
  .label__badge-count { display: block; font-size: 22px; line-height: 22px; }
  .label__badge-unit { display: block; font-size: 14px; line-height: 18px; }

  .label--liver .label__title,
  .label--liver .label__subtitle { color: var(--liver); }
  .label--liver .label__badge { left: 335px; background: linear-gradient(90deg, var(--liver-badge-a), var(--liver-badge-b)); }

  .label--tummy .label__title,
  .label--tummy .label__subtitle { color: var(--tummy); }
  .label--tummy .label__badge { left: 377px; top: 153px; background: linear-gradient(90deg, var(--tummy-badge-a), var(--tummy-badge-b)); }

  .label--hormone .label__title { color: var(--hormone); }
  .label--hormone .label__badge { left: 377px; top: 153px; background: linear-gradient(90deg, var(--hormone-badge-a), var(--hormone-badge-b)); }

  .label--sugar .label__title { color: var(--sugar); }
  .label--sugar .label__badge {
    left: 377px; top: 164px; width: 132px; height: 42px; padding-top: 2px;
    background: linear-gradient(90deg, var(--sugar-badge-a), var(--sugar-badge-b));
  }
  .label--sugar .label__badge-count { font-size: 20px; line-height: 20px; }
  .label--sugar .label__badge-unit { font-size: 13px; line-height: 16px; }
</style>
</head>
<body>

  <section class="label label--liver">
    <div class="label__art" role="img" aria-label="Soft lilac flowers and petals"></div>
    <svg class="label__wave" viewBox="0 0 733 243" aria-hidden="true">
      <path d="M0,243 C180,195 420,218 580,220 C670,221 715,208 733,196 L733,243 Z" fill="var(--white)"/>
      <path d="M0,243 C180,203 420,226 580,228 C670,229 715,216 733,204 L733,243 Z" fill="var(--liver-band)"/>
    </svg>
    <h2 class="label__title">Hepaline</h2>
    <p class="label__subtitle">Rejuvenating Cleanse &amp; Detox Formula*<br>Dietary Supplement</p>
    <div class="label__badge"><span class="label__badge-count">120</span><span class="label__badge-unit">VEGETABLE CAPSULES</span></div>
  </section>

  <section class="label label--tummy">
    <div class="label__art" role="img" aria-label="Pink blossoms and baby's breath"></div>
    <svg class="label__wave" viewBox="0 0 733 243" aria-hidden="true">
      <path d="M0,243 C180,195 420,218 580,220 C670,221 715,208 733,196 L733,243 Z" fill="var(--white)"/>
      <path d="M0,243 C180,203 420,226 580,228 C670,229 715,216 733,204 L733,243 Z" fill="var(--tummy-band)"/>
    </svg>
    <h2 class="label__title">Calmbelle</h2>
    <p class="label__subtitle">Oxygenating Colon Cleanse*<br>Dietary Supplement</p>
    <div class="label__badge"><span class="label__badge-count">90</span><span class="label__badge-unit">VEGETABLE CAPSULES</span></div>
  </section>

  <section class="label label--hormone">
    <div class="label__art" role="img" aria-label="Green eucalyptus leaves with fine gold lines"></div>
    <svg class="label__wave" viewBox="0 0 733 243" aria-hidden="true">
      <path d="M0,243 C180,195 420,218 580,220 C670,221 715,208 733,196 L733,243 Z" fill="var(--white)"/>
      <path d="M0,243 C180,203 420,226 580,228 C670,229 715,216 733,204 L733,243 Z" fill="var(--hormone-band)"/>
    </svg>
    <h2 class="label__title">Equibloom</h2>
    <p class="label__subtitle">Supports Healthy Hormone Levels*<br>Dietary Supplement</p>
    <div class="label__badge"><span class="label__badge-count">60</span><span class="label__badge-unit">VEGETABLE CAPSULES</span></div>
  </section>

  <section class="label label--sugar">
    <div class="label__art" role="img" aria-label="Translucent blue lily flowers"></div>
    <svg class="label__wave" viewBox="0 0 733 243" aria-hidden="true">
      <path d="M0,243 C180,195 420,218 580,220 C670,221 715,208 733,196 L733,243 Z" fill="var(--white)"/>
      <path d="M0,243 C180,203 420,226 580,228 C670,229 715,216 733,204 L733,243 Z" fill="var(--sugar-band)"/>
    </svg>
    <h2 class="label__title">Glucorra</h2>
    <p class="label__subtitle">Supports Healthy Blood Glucose Levels*<br>Dietary Supplement</p>
    <div class="label__badge"><span class="label__badge-count">60</span><span class="label__badge-unit">Vegetable Capsules</span></div>
  </section>

</body>
</html>
```